Manufacturer of heath beverages and shooters requires label design

We require a label design for our first beverage we are launching in the US market under the brand Quorra Mixx. Our manufacturing facility is based in California, USA.

The name of the beverage is FenlowTum, and is a health beverage to support gut health. The final design should communicate aspects such as life, energy, nature, well-being, and good health. Logo and dimensions of the label attached.
Updates

Target Market(s)

This should appeal to a broad audience across ages and genders. We are targeting individuals who are already health conscious, as well as those who are trying to improve their health.

Industry/Entity Type

Health And Wellness

Requirements
Must have
• Info that must be included
• Attached logo
• The name "FenlowTum"
• Under the name: "Natural digestive aid and overall gut health support"
• An "Organic" icon
• Caffeine-free
• 2 fl oz (59ml)
• Shake well
• Directions:
• Add contents of bottle to 6 oz warm water. Drink first thing in the morning or after a heavy meal. For best results, consume daily.
• Leave space for the nutrition facts and ingredients (will be provided to add to the winning design).
Should not have
• No images of fruit. This is not a fruit beverage.

```html
<!DOCTYPE html>
<html lang="en">
<head>
<meta charset="UTF-8">
<title>FenlowTum Label – Quorra Mixx</title>
<link rel="stylesheet" href="https://fonts.googleapis.com/css2?family=Cabin+Condensed:wght@500&family=Marcellus&family=Marcellus+SC&family=Montserrat:wght@300;400&family=Archivo+Black&display=swap">
<style>
  :root {
    --orange: #f15a29;
    --orange-deep: #d9401a;
    --green-brand: #7cc142;
    --badge-green: #2f5a3c;
    --product-brown: #6a5310;
    --ink: #1d1a16;
    --heading-grey: #4a4540;
    --shake-green: #3d5a1c;
    --tagline-grey: #6f6f6f;
  }
  * { margin: 0; padding: 0; box-sizing: border-box; }
  html, body { width: 1200px; height: 985px; overflow: hidden; background: #ffffff; }
  .label { position: relative; width: 1200px; height: 985px; overflow: hidden; }

  .backdrop {
    position: absolute; inset: 0;
    background:
      radial-gradient(ellipse 520px 380px at 560px 560px, rgba(255,240,210,0.75), rgba(255,240,210,0) 70%),
      linear-gradient(180deg, #fbfbfa 0%, #f3efe6 22%, #efe6d3 45%, #efe0bd 62%, #d9d39a 76%, #a9b860 88%, #8ca645 100%);
  }
  .info-panel {
    position: absolute; left: 768px; top: 0; width: 432px; height: 985px;
    background: linear-gradient(180deg, rgba(250,243,238,0.85), rgba(250,240,225,0.6) 70%, rgba(250,235,200,0.35));
    border-left: 4px solid rgba(255,255,255,0.7);
  }
  .shapes { position: absolute; inset: 0; }

  .brand-name {
    position: absolute; left: 330px; top: 70px; width: 420px; text-align: center;
    font-family: "Montserrat", sans-serif; font-weight: 400; font-size: 62px;
    color: var(--orange); letter-spacing: 1px;
  }
  .brand-tagline {
    position: absolute; left: 408px; top: 160px;
    font-family: "Montserrat", sans-serif; font-weight: 300; font-size: 20px;
    letter-spacing: 6px; color: var(--tagline-grey);
  }

  .product-name {
    position: absolute; right: 465px; top: 700px;
    font-family: "Archivo Black", sans-serif; font-size: 64px; letter-spacing: -2px;
    color: var(--product-brown);
  }
  .product-sub {
    position: absolute; font-family: "Montserrat", sans-serif; font-weight: 400;
    font-size: 19px; color: var(--ink);
  }
  .product-sub.line-one { left: 347px; top: 779px; }
  .product-sub.line-two { right: 447px; top: 807px; }

  .caffeine {
    position: absolute; right: 444px; top: 905px;
    font-family: "Marcellus SC", serif; font-size: 28px; letter-spacing: 1px;
    color: var(--orange-deep);
  }
  .volume {
    position: absolute; right: 442px; top: 948px;
    font-family: "Marcellus", serif; font-size: 23px; color: var(--ink); font-weight: 700;
  }

  .panel-heading {
    position: absolute; left: 795px;
    font-family: "Marcellus", serif; font-size: 29px; color: var(--heading-grey);
  }
  .heading-directions { top: 58px; }
  .heading-nutrition { top: 382px; }
  .heading-ingredients { top: 688px; }

  .directions-text {
    position: absolute; left: 796px; top: 143px; width: 360px;
    font-family: "Cabin Condensed", sans-serif; font-weight: 500; font-size: 26px;
    line-height: 34.5px; letter-spacing: -0.5px; color: var(--ink);
  }

  .shake {
    position: absolute; left: 800px; top: 953px;
    font-family: "Marcellus SC", serif; font-size: 25px; color: var(--shake-green);
  }
</style>
</head>
<body>
<div class="label">
  <div class="backdrop" role="img" aria-label="Sunlit meadow with tall green grass and a woman in a light dress raising her arms to the sky"></div>
  <div class="info-panel"></div>

  <svg class="shapes" width="1200" height="985" viewBox="0 0 1200 985" aria-hidden="true">
    <!-- white sky wash behind brand area -->
    <path d="M0 0 H768 V195 C560 240 260 240 0 170 Z" fill="#ffffff" opacity="0.55"/>
    <!-- grey fine swoosh -->
    <path d="M0 185 C230 270 520 300 768 210" fill="none" stroke="#9a9a9a" stroke-width="2.5"/>
    <!-- orange brand swoosh -->
    <path d="M0 66 C160 170 420 260 768 196 L768 208 C420 290 150 230 0 120 Z" fill="var(--orange)"/>
    <!-- faint swoosh on info panel -->
    <path d="M768 196 C960 170 1140 240 1190 455" fill="none" stroke="#d94030" stroke-width="10" opacity="0.35"/>
    <!-- organic badge -->
    <circle cx="706" cy="235" r="55" fill="var(--badge-green)"/>
    <circle cx="706" cy="235" r="44" fill="#ffffff"/>
    <circle cx="706" cy="235" r="38" fill="none" stroke="var(--badge-green)" stroke-width="2"/>
  </svg>

  <div class="brand-name">Quorra Mixx</div>
  <div class="brand-tagline">Be Well. Live Well.</div>

  <div class="product-name">FenlowTum</div>
  <div class="product-sub line-one">Natural digestive aid</div>
  <div class="product-sub line-two">and overall gut health support</div>

  <div class="caffeine">Caffeine-free</div>
  <div class="volume">2 fl oz (59ml)</div>

  <div class="panel-heading heading-directions">Directions:</div>
  <div class="directions-text">Add contents of bottle to 6 oz warm water. Drink first thing in the morning or after a heavy meal. For best results, consume daily.</div>
  <div class="panel-heading heading-nutrition">Nutrition facts</div>
  <div class="panel-heading heading-ingredients">Ingredients</div>

  <div class="shake">SHAKE WELL BEFORE USE</div>
</div>
</body>
</html>
```